Reworking our Ayurvedic Tea Boxes with Mordern and New look.

We are a Tea Wholesale company for retailers and health food stores. We have currently a Ayurvedic wellness tea line needs an updated packaging. We would like to see new modern, clean and beautiful new fresh look. Our current packaging can be seen at http://leafmerchantco.ca/c/7720164/1/calm-blends.html

We are going to launch various categories in the loose leaf tea line. This is just the first step. At present 9 different exsit in the wellnes line.
Updates

Target Market(s)

Health Food Stores, Specialty Food Stores, Grocery Stores.

Industry/Entity Type

It Company

Requirements
Must have
• - Name of the of the tea type should be clearly visible.
• - A modern fresh look. Not to heavy with design work.
Nice to have
• Box size is 8 cm (L) X 4.5 cm (W) X 15cm (H)

```html
<!DOCTYPE html>
<html lang="en">
<head>
<meta charset="utf-8">
<title>Twilight Hour – Ayurvedic Tea Box Front</title>
<link rel="stylesheet" href="https://fonts.googleapis.com/css2?family=Dosis:wght@600&family=Great+Vibes&family=Questrial&display=swap">
<style>
  :root {
    --plum: #a8168f;
    --lime: #b8e021;
    --white: #ffffff;
  }
  * { margin: 0; padding: 0; box-sizing: border-box; }
  html, body {
    width: 1200px;
    height: 2250px;
    overflow: hidden;
    background: var(--plum);
  }
  .box-front {
    position: relative;
    width: 1200px;
    height: 2250px;
    background: var(--plum);
    color: var(--white);
    overflow: hidden;
  }
  .mandala-ornament {
    position: absolute;
    left: 40px;
    top: -500px;
    width: 1120px;
    height: 1160px;
    border-radius: 50%;
    background: radial-gradient(circle at 50% 50%,
      rgba(184, 224, 33, 0.45) 0%,
      rgba(184, 224, 33, 0.30) 50%,
      rgba(184, 224, 33, 0.12) 80%,
      rgba(184, 224, 33, 0) 100%);
  }
  .line-name {
    position: absolute;
    top: 668px;
    width: 100%;
    text-align: center;
    font-family: "Dosis", sans-serif;
    font-weight: 600;
    font-size: 114px;
    line-height: 1;
  }
  .tea-name {
    position: absolute;
    top: 905px;
    width: 100%;
    text-align: center;
    font-family: "Great Vibes", cursive;
    font-weight: 400;
    font-size: 205px;
    line-height: 1.2;
    white-space: nowrap;
  }
  .tea-format {
    position: absolute;
    top: 1232px;
    width: 100%;
    text-align: center;
    font-family: "Questrial", sans-serif;
    font-size: 72px;
    letter-spacing: 1px;
    line-height: 1;
  }
  .caffeine-note {
    position: absolute;
    top: 1330px;
    width: 100%;
    text-align: center;
    font-family: "Questrial", sans-serif;
    font-size: 50px;
    line-height: 1;
  }
  .label-curves {
    position: absolute;
    left: 0;
    top: 0;
    width: 1200px;
    height: 2250px;
  }
  .label-curves .panel { fill: var(--white); }
  .label-curves .swoosh { fill: var(--lime); }
  .brand-name {
    position: absolute;
    left: 56px;
    top: 2070px;
    font-family: "Questrial", sans-serif;
    font-size: 62px;
    letter-spacing: 3px;
    text-transform: uppercase;
    line-height: 1;
    white-space: nowrap;
  }
  .net-weight {
    position: absolute;
    left: 56px;
    top: 2162px;
    font-family: "Questrial", sans-serif;
    font-size: 50px;
    line-height: 1;
    white-space: nowrap;
  }
</style>
</head>
<body>
  <main class="box-front">
    <div class="mandala-ornament" role="img" aria-label="Lime green line-art mandala ornament"></div>

    <h2 class="line-name">Ayurvedic Tea</h2>
    <h1 class="tea-name">Twilight Hour</h1>
    <p class="tea-format">LOOSE LEAF TEA</p>
    <p class="caffeine-note">Caffeine Free / Sans Cafeine</p>

    <svg class="label-curves" viewBox="0 0 1200 2250" aria-hidden="true">
      <path class="swoosh" d="M680 1592 C 850 1500, 1020 1450, 1200 1432 L1200 1478 C 1020 1490, 860 1530, 680 1592 Z"/>
      <path class="panel" d="M420 1966 C 540 1720, 850 1560, 1200 1520 L1200 2004 C 900 1995, 640 1985, 420 1966 Z"/>
    </svg>

    <p class="brand-name">Leaf Merchant</p>
    <p class="net-weight">Nett Weight 3.5 oz/Poids Net 100 g</p>
  </main>
</body>
</html>
```